Custom CV (resume) Template in Word 2013

We are a boutique Marketing Agency that specialises in outsourcing our staff to work with clients internally. As such it is imperitive that we are able to communicate the capabilities and experience of our staff to our clients in a simple, succinct, and engaging manner. In this endeavour we look to commission a CV (resume) template that utilises our intellectual property, logo, and corporate colours to be used for existing and future staff in order to better market them to clients.
Our firm places a high value on being a ‘one-page’ business. As such we would strongly prefer that all submissions are limited to a single sheet. Designs must include the following components:
•	Place for Candidates Name
•	Place for our logo (logo is attached)
•	Place for our contact information
•	A section for an introduction or blurb about the candidate
•	A table (or similar) for listing previous experience and a summary of each experience
•	A table (or similar) where candidates can list the relevant industries in which they have experience
The following are our brand colours:
•	C: 56 M:0 Y:100 K:27        R:94 G:151 B:50
•	C:0 M:10 Y:33 K:72           R:105 G:94 B:74
•	C:0 M:8 Y:26 K:57              R:135 G:124 B:105
This template must be delivered in Word 2010 or 2013. As long as the parameters above are met we are flexible to the design elements.
I have also attached an example from one of our competitors and have removed their details for their privacy as an example of something we are looking for.

Boutique

```html
<!DOCTYPE html>
<html lang="en">
<head>
<meta charset="utf-8">
<title>Candidate CV Template</title>
<link rel="stylesheet" href="https://fonts.googleapis.com/css2?family=Open+Sans:ital,wght@0,700;1,700&family=Source+Sans+3:wght@400&display=swap">
<style>
  :root {
    --backdrop: #2b2927;
    --paper-top: #ffffff;
    --paper-bottom: #efeee6;
    --name-band: #dfe9b3;
    --brand-green: #5e9732;
    --brand-brown: #695e4a;
    --brand-taupe: #877c69;
    --ink: #1c1c1c;
    --white: #ffffff;
    --photo-light: #d9c9b8;
    --photo-dark: #3a2f2a;
  }
  * { margin: 0; padding: 0; box-sizing: border-box; }
  html, body {
    width: 1200px; height: 899px; overflow: hidden;
    background: var(--backdrop);
  }
  .cv-page {
    position: absolute; left: 91px; top: 96px;
    width: 1031px; height: 728px; overflow: hidden;
    background: linear-gradient(to bottom, var(--paper-top) 0%, var(--paper-top) 20%, var(--paper-bottom) 100%);
    font-family: "Source Sans 3", "Myriad Pro", Arial, sans-serif;
    color: var(--ink);
  }
  .name-band {
    position: absolute; left: 0; top: 46px; width: 100%; height: 84px;
    background: var(--name-band);
  }
  .bio-badge {
    position: absolute; left: 25px; top: 23px; width: 131px; height: 191px;
  }
  .bio-badge svg { position: absolute; inset: 0; }
  .candidate-photo {
    position: absolute; left: 13px; top: 10px; width: 107px; height: 126px;
    background: linear-gradient(to bottom, var(--photo-light) 0%, #c9a98f 50%, var(--photo-dark) 100%);
  }
  .bio-label {
    position: absolute; left: 0; top: 140px; width: 100%; text-align: center;
    font-family: "Open Sans", Arial, sans-serif; font-weight: 700; font-style: italic;
    font-size: 19px; color: var(--white);
  }
  .candidate-name {
    position: absolute; left: 177px; top: 63px;
    font-family: "Open Sans", Arial, sans-serif; font-weight: 700; font-style: italic;
    font-size: 38px; line-height: 50px; color: #111;
  }
  .agency-mark {
    position: absolute; left: 760px; top: 58px; height: 56px;
    display: flex; align-items: center; gap: 12px;
  }
  .agency-mark .dot {
    width: 30px; height: 30px; border-radius: 50%; background: var(--brand-green);
  }
  .agency-mark .agency-name {
    font-family: "Open Sans", Arial, sans-serif; font-weight: 700;
    font-size: 40px; color: var(--brand-green); letter-spacing: -1px;
  }
  .bio-text {
    position: absolute; left: 28px; top: 232px; width: 572px;
    font-size: 17.5px; line-height: 20.8px;
    hyphens: auto; -webkit-hyphens: auto;
  }
  .bio-text p.lead { text-indent: 44px; }
  .bio-text p.spaced { margin-top: 20.8px; }
  .side-column {
    position: absolute; left: 643px; top: 0; width: 388px; height: 100%;
  }
  .section-head {
    position: absolute; left: 0; width: 388px;
    padding: 0 50px 0 22px;
    display: flex; align-items: center;
    font-family: "Open Sans", Arial, sans-serif; font-weight: 700; font-style: italic;
    font-size: 19px; line-height: 22px; color: var(--white); text-transform: uppercase;
  }
  .section-head::after {
    content: ""; position: absolute; left: 0; top: 100%;
    width: 66px; height: 20px; background: inherit;
    clip-path: polygon(0 0, 100% 0, 0 100%);
  }
  .head-experience { top: 149px; height: 35px; background: var(--brand-green); }
  .head-previous { top: 340px; height: 59px; background: var(--brand-taupe); }
  .head-contact { top: 599px; height: 35px; background: var(--brand-brown); }
  .section-body {
    position: absolute; left: 1px; width: 372px;
    font-size: 17.5px; line-height: 20.8px;
  }
  .body-experience { top: 212px; }
  .body-previous { top: 422px; }
  .body-contact { top: 652px; }
</style>
</head>
<body>
<main class="cv-page">
  <div class="name-band"></div>

  <div class="bio-badge">
    <svg width="131" height="191" viewBox="0 0 131 191" aria-hidden="true">
      <polygon points="0,0 131,0 131,160 65.5,191 0,160" fill="#695e4a"/>
    </svg>
    <div class="candidate-photo" role="img" aria-label="Candidate portrait photo"></div>
    <div class="bio-label">BIO</div>
  </div>

  <h1 class="candidate-name">Candidates Name</h1>

  <div class="agency-mark">
    <span class="dot"></span>
    <span class="agency-name">Tall Grove</span>
  </div>

  <section class="bio-text">
    <p class="lead">Lorem Ipsum is simply dummy text of the printing and typesetting industry. Lorem Ipsum has been the industry's standard dummy text ever since the 1500s, when an unknown printer took a galley of type and scrambled it to make a type specimen book. It has survived not only five centuries, but also the leap into electronic typesetting, remaining essentially unchanged. It was popularised in the 1960s with the release of Marlowe sheets containing Lorem Ipsum passages, and more recently with desktop publishing software like Fenwick Layout including versions of Lorem Ipsum.</p>
    <p>Lorem Ipsum is simply dummy text of the printing and typesetting industry. Lorem Ipsum has been the industry's standard dummy text ever since the 1500s, when an unknown printer took a galley of type and scrambled it to make a type specimen book. It has survived not only five centuries, but also the leap into electronic typesetting, remaining essentially unchanged. It was popularised in the 1960s with the release of Marlowe sheets containing Lorem Ipsum passages, and more recently with desktop publishing software like Fenwick Layout including versions of Lorem Ipsum.</p>
    <p class="spaced">Lorem Ipsum is simply dummy text of the printing and typesetting industry. Lorem Ipsum has been the industry's standard dummy text ever since the 1500s, when an unknown printer took a galley of type and scrambled it to make a type specimen book. It has survived not only five centuries, but also the leap into electronic typesetting, remaining essentially unchanged. It was popularised in</p>
  </section>

  <aside class="side-column">
    <h2 class="section-head head-experience">Experience</h2>
    <p class="section-body body-experience">Lorem Ipsum is simply dummy text of the printing and typesetting industry. Lorem Ipsum has been the industry's standard dummy text ever since the 1500s, when an unknown printer took a galley of type and scrambled it to make a type specimen</p>

    <h2 class="section-head head-previous">Previous experience and a summary of each expierence</h2>
    <p class="section-body body-previous">Lorem Ipsum is simply dummy text of the printing and typesetting industry. Lorem Ipsum has been the industry's standard dummy text ever since the 1500s, when an unknown printer took a galley of type and scrambled it to make a type specimen book. It has survived not only five centuries, but also the leap into electronic typesetting, remaining</p>

    <h2 class="section-head head-contact">Contact information</h2>
    <p class="section-body body-contact">Lorem Ipsum is simply dummy text of the printing and typesetting industry. Lorem Ipsum has been</p>
  </aside>
</main>
</body>
</html>
```